Business Card Design Project

Use our current logo. Clean design.

Industry/Entity Type

Business

Requirements
Must have
• Marisela DUCRANTE
M. Law
Managing Partner

Velotrana AG
Brunnmattweg 274
CH-3097 Liebefeld

M. +41 79 418 26 97
T. +41 31 742 19 04
F. +41 31 742 19 38

m.ducrante@velotrana.example
www.velotrana.example

```html
<!DOCTYPE html>
<html lang="en">
<head>
<meta charset="utf-8">
<title>Velotrana AG – Business Card</title>
<link rel="stylesheet" href="https://fonts.googleapis.com/css2?family=Tinos&display=swap">
<style>
  :root {
    --page: #ffffff;
    --front-edge: #000000;
    --front-mid: #58585a;
    --brand-red: #ed1c24;
    --bar-grey: #808084;
    --bar-dark: #3a3a3c;
    --text-grey: #555555;
    --ink: #000000;
    --rule: #555555;
  }
  * { margin: 0; padding: 0; box-sizing: border-box; }
  html, body {
    width: 1200px; height: 1000px; overflow: hidden;
    background: var(--page);
    font-family: "Tinos", "Times New Roman", serif;
  }
  .canvas { position: relative; width: 1200px; height: 1000px; }

  .card-front {
    position: absolute; left: 288px; top: 73px; width: 614px; height: 375px;
    background: linear-gradient(90deg, var(--front-edge) 0%, #1e1e1f 12%, var(--front-mid) 54%, #2a2a2b 88%, var(--front-edge) 100%);
    display: flex; align-items: center; justify-content: center;
  }
  .front-name {
    color: #ffffff; font-size: 54px; letter-spacing: 4px;
    font-weight: 400; margin-top: 20px;
  }

  .card-back {
    position: absolute; left: 289px; top: 521px; width: 615px; height: 376px;
    border: 1px solid var(--rule); background: #ffffff;
  }
  .top-bands { position: absolute; left: 0; top: 0; width: 100%; height: 26px; display: flex; }
  .band-red { width: 109px; background: var(--brand-red); }
  .band-grey { width: 199px; background: var(--bar-grey); }
  .band-dark { flex: 1; background: var(--bar-dark); }

  .back-name {
    position: absolute; left: 27px; top: 104px;
    font-size: 25px; letter-spacing: 2px; color: var(--ink);
  }
  .divider {
    position: absolute; left: 348px; top: 63px; width: 1px; height: 231px;
    background: var(--rule);
  }
  .holder {
    position: absolute; right: 283px; top: 224px; text-align: right; white-space: nowrap;
  }
  .holder-name { color: var(--brand-red); font-size: 19px; line-height: 26px; }
  .holder-role { color: var(--ink); font-size: 15px; line-height: 20px; margin-right: 4px; }

  .contact {
    position: absolute; left: 369px; color: var(--text-grey);
    font-size: 16px; line-height: 26px;
  }
  .address { top: 88px; }
  .phones { top: 195px; }

  .web-links {
    position: absolute; left: 0; right: 0; top: 316px; text-align: center;
    font-size: 16px; line-height: 22px;
  }
  .email { color: var(--text-grey); }
  .website { color: var(--brand-red); }
</style>
</head>
<body>
<div class="canvas">
  <section class="card-front">
    <div class="front-name">VELOTRANA</div>
  </section>

  <section class="card-back">
    <div class="top-bands">
      <div class="band-red"></div>
      <div class="band-grey"></div>
      <div class="band-dark"></div>
    </div>

    <div class="back-name">VELOTRANA</div>

    <div class="holder">
      <div class="holder-name">Marisela DUCRANTE, M. Law</div>
      <div class="holder-role">Managing Partner</div>
    </div>

    <div class="divider"></div>

    <div class="contact address">
      <div>Velotrana AG</div>
      <div>Brunnmattweg 274</div>
      <div>CH-3097 Liebefeld</div>
    </div>
    <div class="contact phones">
      <div>M. +41 79 418 26 97</div>
      <div>T. +41 31 742 19 04</div>
      <div>F. +41 31 742 19 38</div>
    </div>

    <div class="web-links">
      <div class="email">m.ducrante@velotrana.example</div>
      <div class="website">www.velotrana.example</div>
    </div>
  </section>
</div>
</body>
</html>
```